Flyer Design Project

I require a double sided flyer in PSD format.
The flyer should look fresh and clean.
The flyer is for an digital marketing company that offers various services. The services are broken down into 3 main categories and the design should reflect this.
All the content is provided in the attached file
Industry/Entity Type
Digital
Requirements
Must have
- Front of the leaflet to be mainly white background with appealing text based questions in the colours in large font with relevant images.
Back if the
3 separate boxes using the colours indicated in the attachment for the services on back of the leafet.
Should not have
- Gradients
Borders on the edges of the design
Vignettes
Black elements
Any text below 10pt
Fancy fonts
Do not use old-style fonts

```html
<!DOCTYPE html>
<html lang="en">
<head>
<meta charset="utf-8">
<title>Novara Flyer – Front</title>
<link rel="stylesheet" href="https://fonts.googleapis.com/css2?family=Open+Sans:wght@400;600;700&display=swap">
<style>
  :root {
    --page-bg: #eceae6;
    --paper: #ffffff;
    --band-dark: #33677f;
    --band-mid: #3f7b97;
    --band-light: #8fb6c9;
    --green: #8ccf2e;
    --gold: #e2a418;
    --navy: #1f3d6b;
    --brand-blue: #2f8fbd;
    --text-grey: #333f4a;
  }
  * { margin: 0; padding: 0; box-sizing: border-box; }
  html, body {
    width: 1200px; height: 1000px; overflow: hidden;
    background: var(--page-bg);
    font-family: "Open Sans", Arial, sans-serif;
  }
  .flyer {
    position: absolute; left: 0; top: 78px;
    width: 1200px; height: 845px;
    background: linear-gradient(115deg, #f3f4f6 0%, #ffffff 35%, #ffffff 100%);
    overflow: hidden;
  }
  .band-top {
    position: absolute; left: 0; top: 0; width: 100%; height: 38px;
    background: linear-gradient(180deg, var(--band-dark) 0 24px, var(--band-mid) 24px 30px, var(--band-light) 30px 38px);
  }
  .band-bottom {
    position: absolute; left: 0; bottom: 0; width: 100%; height: 93px;
    background: linear-gradient(180deg, var(--band-mid) 0 12px, var(--band-dark) 12px 100%);
    color: #fff;
  }
  .web-address {
    position: absolute; left: 27px; top: 40px;
    font-size: 16px; font-weight: 600;
  }
  .call-to-action {
    position: absolute; right: 34px; top: 30px;
    font-size: 17px; font-weight: 600; white-space: nowrap;
  }
  .call-to-action .free { font-size: 27px; font-weight: 700; }
  .call-to-action .phone { font-size: 29px; font-weight: 600; margin-left: 8px; }

  .headline {
    position: absolute; left: 370px; top: 93px; width: 500px; z-index: 2;
    text-align: center; color: var(--green); font-weight: 600;
    text-shadow: 0 2px 3px rgba(0,0,0,0.12); line-height: 1.15; white-space: nowrap;
  }
  .headline .are { font-size: 59px; }
  .headline .customers { font-size: 52px; }
  .headline .online { font-size: 40px; }

  .stat-question {
    position: absolute; left: 44px; top: 261px;
    color: var(--navy); font-weight: 600; white-space: nowrap;
    text-shadow: 0 2px 3px rgba(0,0,0,0.12);
  }
  .stat-question .lead { font-size: 43px; line-height: 50px; }
  .stat-question .line { font-size: 33px; line-height: 46px; }
  .stat-question .close { font-size: 55px; line-height: 60px; }

  .growth-question {
    position: absolute; left: 1032px; top: 258px; transform: translateX(-50%);
    color: var(--gold); font-weight: 600; text-align: center;
    text-shadow: 0 2px 3px rgba(0,0,0,0.12); line-height: 1.05; white-space: nowrap;
  }
  .growth-question .do-you { font-size: 74px; line-height: 1; }
  .growth-question .need { font-size: 47px; }
  .growth-question .more { font-size: 38px; }
  .growth-question .customers { font-size: 47px; }
  .growth-question .business { font-size: 26px; margin-top: 8px; }

  .team-illustration {
    position: absolute; left: 398px; top: 294px; width: 472px; height: 360px;
    background: linear-gradient(180deg, rgba(31,95,160,0.85) 0%, rgba(127,211,234,0.75) 75%, rgba(127,211,234,0) 100%);
    border-radius: 6px;
  }
  .tagline {
    position: absolute; left: 620px; top: 660px; transform: translateX(-50%);
    font-size: 20px; font-weight: 600; color: var(--text-grey); white-space: nowrap;
  }
  .brand {
    position: absolute; left: 905px; top: 640px;
    display: flex; align-items: center; gap: 14px;
  }
  .brand-square { width: 30px; height: 30px; background: var(--brand-blue); }
  .brand-name {
    font-size: 50px; font-weight: 600; color: var(--brand-blue); letter-spacing: 1px;
  }
</style>
</head>
<body>
  <main class="flyer">
    <div class="band-top"></div>

    <div class="team-illustration" role="img" aria-label="Silhouettes of a group of business people standing in a row with reflections, in blue tones"></div>

    <h1 class="headline">
      <div class="are">Are</div>
      <div class="customers">Your Customers</div>
      <div class="online">Finding You Online?</div>
    </h1>

    <div class="stat-question">
      <div class="lead">Did You Know</div>
      <div class="line">85% of Consumers</div>
      <div class="line">Use The Internet</div>
      <div class="line">To Find Businesses</div>
      <div class="close">Like Yours?</div>
    </div>

    <div class="growth-question">
      <div class="do-you">Do You</div>
      <div><span class="need">Need</span> <span class="more">More</span></div>
      <div class="customers">Customers</div>
      <div class="business">For Your Business?</div>
    </div>

    <p class="tagline">“ Let us help you grow your business online ”</p>

    <div class="brand">
      <span class="brand-square"></span>
      <span class="brand-name">NOVARA</span>
    </div>

    <footer class="band-bottom">
      <span class="web-address">www.novara-digital.co.uk</span>
      <span class="call-to-action">Call for a <span class="free">FREE</span> consultation <span class="phone">0121 555 0148</span></span>
    </footer>
  </main>
</body>
</html>
```